I need to redesign this website. Modern Fun Professional Redesign For www.JollyPerkHub.com = New Name www.ClaimVouchly.com

Use existing content as it is on website exactly and we will revise after initial mock ups.

The new name will be ClaimVouchly.com please make a quick logo for this site too while redesigning.

Make it look like an official website....

Target Market(s)

Consumers that are redeeming certificates that businesses gave to them as a gift for customer loyalty,e tc.

Industry/Entity Type

It Professional

Logo Text

www.ClaimVouchly.com

Number of Pages Required

4 page

Colors

Designer to choose colors to be used in the design.

Requirements
Must have
• Must look professional, build trust and credibility.
Nice to have
• open
Should not have
• open

```html
<!DOCTYPE html>
<html lang="en">
<head>
<meta charset="utf-8">
<title>ClaimVouchly.com – The Redemption Source</title>
<link rel="stylesheet" href="https://fonts.googleapis.com/css2?family=Raleway:wght@400;500;600;700;800&display=swap">
<style>
:root{
  --accent:#f7a583;
  --accent-dark:#ef8f69;
  --ink:#222222;
  --muted:#555555;
  --light:#ffffff;
  --panel:#ebebeb;
  --footer:#3b3b3b;
  --footer-bottom:#2b2b2b;
  --hero-a:#5b6770;
  --hero-b:#2c333a;
}
*{box-sizing:border-box;margin:0;padding:0}
html,body{width:1200px;height:2400px;overflow:hidden}
body{font-family:"Raleway",Arial,sans-serif;color:var(--ink);background:var(--light);position:relative}

/* Header + hero */
.hero{position:absolute;left:0;top:0;width:1200px;height:740px;overflow:hidden}
.hero-photo{position:absolute;inset:0;background:linear-gradient(135deg,#8b949a 0%,var(--hero-a) 35%,var(--hero-b) 75%,#1f2428 100%)}
.hero-shade{position:absolute;inset:0;background:rgba(20,24,28,.35)}
.brand{position:absolute;left:48px;top:24px;display:flex;align-items:center;gap:16px;color:var(--light);font-weight:700;font-size:30px}
.brand-mark{width:28px;height:28px;background:var(--accent)}
.main-nav{position:absolute;right:36px;top:30px;display:flex;gap:22px;font-size:20px;font-weight:500;text-transform:uppercase}
.main-nav a{color:var(--light);text-decoration:none}
.main-nav a.active{color:var(--accent)}
.hero-copy{position:absolute;left:0;top:150px;width:1200px;text-align:center;color:var(--light);text-transform:uppercase}
.hero-title{font-size:56px;font-weight:700;letter-spacing:1px}
.hero-sub{font-size:26px;font-weight:500;margin-top:10px;line-height:40px}
.redeem-form{position:absolute;left:290px;top:336px;display:flex;height:72px}
.redeem-input{width:450px;height:72px;background:var(--light);border:none;font-family:inherit;font-size:18px;padding-left:22px;color:#999;display:flex;align-items:center}
.redeem-btn{width:172px;height:72px;background:var(--accent);color:var(--light);font-size:34px;font-weight:600;display:flex;align-items:center;justify-content:center}

/* About */
.about{position:absolute;left:0;top:760px;width:1200px;height:460px;background:var(--panel)}
.section-heading{font-size:34px;font-weight:800;text-transform:uppercase}
.about .section-heading{position:absolute;left:40px;top:28px}
.heading-rule{position:absolute;left:40px;top:80px;width:64px;height:4px;background:var(--accent)}
.about-text{position:absolute;left:40px;top:118px;width:690px;font-size:16px;line-height:22px;text-transform:uppercase;color:#333}
.about-text p{margin-bottom:22px}
.read-more{position:absolute;left:484px;top:320px;padding:8px 14px;background:var(--light);border:2px solid #999;font-size:16px;font-weight:700;color:var(--ink)}
.about-brand{position:absolute;left:820px;top:100px;width:280px;height:280px;background:var(--light);border:3px solid var(--accent);border-radius:12px;display:flex;flex-direction:column;align-items:center;justify-content:center;gap:20px;font-size:30px;font-weight:700;color:var(--ink)}
.about-brand .brand-mark{width:56px;height:56px}

/* Testimonials */
.testimonials{position:absolute;left:0;top:1260px;width:1200px;height:400px;background:var(--accent);color:var(--light);text-align:center}
.testimonials .section-heading{margin-top:28px;font-size:38px;font-weight:700}
.testimonials .rule{width:64px;height:3px;background:var(--light);margin:12px auto 0}
.quote{width:1120px;margin:34px auto 0;font-size:24px;line-height:52px;text-transform:uppercase;letter-spacing:.5px}
.quote-author{margin-top:18px;font-size:18px;line-height:30px;text-transform:uppercase}
.quote-author strong{display:block;font-weight:700}
.dots{display:flex;justify-content:center;gap:14px;margin-top:14px}
.dots span{width:34px;height:34px;border:2px solid rgba(255,255,255,.8);border-radius:50%}

/* Newsletter */
.newsletter{position:absolute;left:0;top:1700px;width:1200px;height:320px;text-align:center}
.newsletter .section-heading{margin-top:76px;font-size:40px;font-weight:700}
.newsletter .rule{width:360px;height:2px;background:#ddd;margin:14px auto 0}
.news-input{width:300px;margin:46px 0 0 380px;text-align:left;font-size:16px;color:#999;border-bottom:2px solid #ccc;padding-bottom:6px}
.send-btn{display:inline-block;background:var(--accent);color:var(--light);font-weight:700;font-size:16px;padding:6px 20px}
.newsletter .send-btn{position:absolute;left:566px;top:234px}

/* Footer */
.site-footer{position:absolute;left:0;top:2048px;width:1200px;height:312px;background:var(--footer);color:var(--light)}
.footer-brand{position:absolute;left:60px;top:26px;width:260px;text-align:center}
.footer-brand .brand-name{display:flex;align-items:center;justify-content:center;gap:10px;font-size:22px;font-weight:700}
.footer-brand .brand-mark{width:18px;height:18px}
.footer-brand p{margin-top:22px;font-size:15px;font-weight:700;line-height:42px;text-transform:uppercase}
.divider{position:absolute;top:40px;width:2px;height:230px;background:#666}
.footer-links{position:absolute;left:540px;top:66px}
.footer-title{font-size:34px;font-weight:600;text-transform:uppercase}
.footer-links ul{list-style:none;margin-top:12px}
.footer-links li{font-size:16px;font-weight:700;line-height:38px;text-transform:uppercase}
.touch{position:absolute;left:900px;top:66px;width:260px}
.touch .footer-title{text-align:center}
.touch-form{display:flex;align-items:center;gap:14px;margin-top:26px}
.touch-input{width:180px;height:36px;background:var(--light);color:#777;font-size:14px;padding:9px 10px}
.social{display:flex;justify-content:center;gap:10px;margin-top:22px}
.social span{width:30px;height:30px;border-radius:50%;background:#8b8b8b}
.copyright{position:absolute;left:0;top:2360px;width:1200px;height:40px;background:var(--footer-bottom);color:var(--light);text-align:center;font-size:16px;font-weight:600;line-height:40px}
</style>
</head>
<body>

<header class="hero">
  <div class="hero-photo" role="img" aria-label="Photo of business people working at a laptop in an office"></div>
  <div class="hero-shade"></div>
  <div class="brand"><span class="brand-mark"></span>ClaimVouchly.com</div>
  <nav class="main-nav">
    <a class="active" href="#">Home</a>
    <a href="#">Contact Us</a>
    <a href="#">Testimonial</a>
    <a href="#">Terms</a>
  </nav>
  <div class="hero-copy">
    <h1 class="hero-title">Welcome to the Redemption Source</h1>
    <p class="hero-sub">Please enter a valid certificate ID in the form below<br>to redeem your certificate and to view FAQ's, terms and locations.</p>
  </div>
  <div class="redeem-form">
    <div class="redeem-input">ENTER...</div>
    <div class="redeem-btn">GO</div>
  </div>
</header>

<section class="about">
  <h2 class="section-heading">About Us:</h2>
  <div class="heading-rule"></div>
  <div class="about-text">
    <p>JollyPerkHub.com is a leading company in travel certificate fulfillment.</p>
    <p>Our goal is to make it easy for you to redeem your certificate and our philosophy is this: "What good is it to receive a gift certificate if you can't use it?"</p>
    <p>If you have any questions about how to redeem a certain certificate, please contact us. We are here to help!</p>
  </div>
  <div class="read-more">Read More</div>
  <div class="about-brand"><span class="brand-mark"></span>ClaimVouchly.com</div>
</section>

<section class="testimonials">
  <h2 class="section-heading">Testimonials:</h2>
  <div class="rule"></div>
  <p class="quote">"Mara was a "saving grace." She followed up and helped me book the vacation and air fare. Mara was positive and did everything she promised to do."</p>
  <div class="quote-author">
    <strong>Lena P.</strong>
    Millbrook, GA<br>
    Added on 05/13/2017 05:24:58 PM
  </div>
  <div class="dots"><span></span><span></span></div>
</section>

<section class="newsletter">
  <h2 class="section-heading">Get Our Newslatter</h2>
  <div class="rule"></div>
  <div class="news-input">Email...</div>
  <div class="send-btn">SEND</div>
</section>

<footer class="site-footer">
  <div class="footer-brand">
    <div class="brand-name"><span class="brand-mark"></span>ClaimVouchly.com</div>
    <p>Lorem ipsum dolor sit amet,<br>consectetur adipiscing elit,<br>sed do eiusmod tempor</p>
  </div>
  <div class="divider" style="left:380px"></div>
  <div class="footer-links">
    <h3 class="footer-title">Links</h3>
    <ul>
      <li>Home</li>
      <li>Contact Us</li>
      <li>Testimonial</li>
      <li>Terms</li>
    </ul>
  </div>
  <div class="divider" style="left:800px"></div>
  <div class="touch">
    <h3 class="footer-title">Touch Us</h3>
    <div class="touch-form">
      <div class="touch-input">EMAIL</div>
      <div class="send-btn">SEND</div>
    </div>
    <div class="social"><span></span><span></span><span></span></div>
  </div>
</footer>
<div class="copyright">copyright all right reserved</div>

</body>
</html>
```